Towing Company Website Towing Basel West

Hello I need a cool website for my towing company. - Home - About us - Parking Enforcement - Repossession - Disaster Recovery - Accident Recovery - Contact So someone would have to install the website on Hostwerk for me. No idea how that works.

Target Market(s)

www.bergungsdienst-talwald.cc

Contact Information for Business Card

Bergungsdienst Talwald Ost
P: 044 927 64 18
F: 044 927 64 19
E: mail@bergungsdienst-talwald.cc
W: www.bergungsdienst-talwald.cc

Lukas Brändle
M: 075 638 49 70

Number of Pages Required

5+ page

Font styles to use
Sans Serif

Colors

Designer to choose colors to be used in the design.

```html
<!DOCTYPE html>
<html lang="de">
<head>
<meta charset="utf-8">
<title>Bergungsdienst Talwald Ost</title>
<link href="https://fonts.googleapis.com/css2?family=Lato:wght@400;700;900&family=Roboto+Condensed:wght@400;700&display=swap" rel="stylesheet">
<style>
:root{
  --red:#e8212b;
  --dark:#2b2b2b;
  --black:#0b0b0d;
  --light:#eeeeee;
  --paper:#f5f5f5;
  --white:#ffffff;
  --text:#444444;
}
*{margin:0;padding:0;box-sizing:border-box}
html,body{width:1200px;height:3291px;overflow:hidden}
body{position:relative;font-family:'Lato',sans-serif;color:var(--text);background:var(--white)}
.abs{position:absolute}
.brand{font-family:'Lato',sans-serif;font-weight:900;color:var(--black);font-size:30px;line-height:1.1}
.brand small{display:block;font-size:22px;text-align:right}
.site-header{left:0;top:0;width:1200px;height:165px;background:var(--white)}
.call-label,.follow-label{font-size:22px;color:var(--red)}
.call-number{font-size:23px;font-weight:700;color:var(--black)}
.social{display:flex;gap:4px}
.social span{width:18px;height:18px;border-radius:50%;background:var(--black)}
.main-nav{left:0;top:165px;width:1200px;height:46px;background:var(--red);display:flex;align-items:center;padding-left:32px;font-size:17px;color:var(--white)}
.main-nav a{color:var(--white);text-decoration:none;padding:0 12px;height:46px;line-height:46px}
.main-nav a.active{background:var(--black);color:var(--red);padding:0 20px}
.hero{left:0;top:211px;width:1200px;height:531px;background:linear-gradient(100deg,#5a4a40 0%,#8a7565 30%,#6e6860 60%,#8c8580 100%)}
.hero-copy{left:700px;top:330px;width:420px;text-align:center;color:var(--white)}
.hero-copy h1{font-weight:400;font-size:38px;line-height:1.25}
.hero-copy hr{width:72px;border:0;border-top:3px solid var(--white);margin:20px auto 14px}
.hero-phone{font-family:'Roboto Condensed',sans-serif;font-weight:700;font-size:66px;color:var(--red)}
.section-title{font-family:'Lato',sans-serif;font-size:38px;font-weight:700;line-height:46px;white-space:nowrap}
.section-title.centered{left:0;width:1200px;text-align:center}
.section-title .accent{color:var(--red)}
.about{left:0;top:742px;width:1200px;height:508px;background:var(--light)}
.photo{background:linear-gradient(135deg,#7fb2dc,#cfd9e3 45%,#b33a30 75%,#3a4c6b)}
.body-text{font-size:13px;line-height:25px;color:#555}
.btn{display:inline-block;background:var(--red);color:var(--white);font-size:12px;text-align:center;height:30px;line-height:30px;text-transform:uppercase}
.services{left:0;top:1250px;width:1200px;height:743px;background:var(--dark)}
.services .section-title{color:var(--white)}
.services .body-text{color:#ddd;text-align:center}
.service{width:230px;text-align:center}
.service .circle{width:220px;height:220px;border-radius:50%;margin:0 auto}
.service h3{font-family:'Roboto Condensed',sans-serif;color:var(--red);font-size:18px;margin-top:30px}
.service p{color:#ddd;font-size:14px;line-height:26px;margin-top:6px}
.service .btn{width:124px;margin-top:20px}
.news{left:0;top:1993px;width:1200px;height:340px;background:var(--paper)}
.col-title{font-weight:700;font-size:25px;color:var(--red);letter-spacing:1px}
.rule{height:1px;background:#ccc}
.pager{display:flex;gap:4px}
.pager span{width:18px;height:18px;border-radius:50%;background:var(--red);color:var(--white);font-size:11px;text-align:center;line-height:18px}
.pager span.dark{background:var(--black)}
.post-title{font-weight:700;font-size:15px;color:var(--black)}
.small-text{font-size:11px;line-height:16px;color:#555}
.contact{left:0;top:2333px;width:1200px;height:560px;background:var(--dark)}
.contact .section-title{color:var(--white)}
.form-card{left:143px;top:2493px;width:915px;height:325px;background:var(--white)}
.field{border:1px solid #ccc;background:#f3f3f3;font-size:12px;color:#999;padding:9px 10px}
.submit{background:var(--red);color:var(--white);font-size:12px;text-align:center;line-height:35px;height:35px}
.newsletter{left:0;top:2893px;width:1200px;height:65px;background:var(--red);color:var(--white)}
.footer{left:0;top:2958px;width:1200px;height:302px;background:var(--black);color:var(--white)}
.footer .brand{color:var(--white)}
.foot-title{font-size:16px;font-weight:700;text-transform:uppercase}
.foot-title .accent{color:var(--red)}
.foot-list{list-style:none;font-size:13px;line-height:26px;color:#ddd}
.foot-list li::before{content:"› ";color:#888}
.foot-info{font-size:13px;line-height:22px;color:#ddd}
.copyright{left:0;top:3260px;width:1200px;height:31px;background:#1a1a1a;color:#bbb;font-size:10px;text-align:center;line-height:31px}
</style>
</head>
<body>

<header class="site-header abs">
  <div class="brand abs" style="left:72px;top:40px">Bergungsdienst<small>Talwald Ost</small></div>
  <div class="abs" style="left:770px;top:58px;text-align:center">
    <div class="call-label">Call Us Now</div>
    <div class="call-number">044 927 64 18</div>
  </div>
  <div class="abs" style="left:946px;top:60px;width:1px;height:52px;background:#999"></div>
  <div class="abs" style="left:985px;top:58px;text-align:center">
    <div class="follow-label">Follow Us</div>
    <div class="social" style="margin-top:6px"><span></span><span></span><span></span><span></span><span></span><span></span></div>
  </div>
</header>

<nav class="main-nav abs">
  <a class="active" href="#">HOME</a>
  <a href="#">ABOUT US</a><span>|</span>
  <a href="#">PARKING ENFORCEMENT</a><span>|</span>
  <a href="#">REPOSSESSION</a><span>|</span>
  <a href="#">BREAKDOWN ASSISTANCE</a><span>|</span>
  <a href="#">SERVICES</a><span>|</span>
  <a href="#">CONTACT US</a>
</nav>

<section class="hero abs" role="img" aria-label="Photo of a worried driver on the phone beside a broken-down car"></section>
<div class="hero-copy abs">
  <h1>Bergungsdienst Talwald Ost hilft in jeder Situation</h1>
  <hr>
  <div class="hero-phone">044 927 64 18</div>
</div>

<section class="about abs">
  <div class="photo abs" role="img" aria-label="Photo of a red tow truck lifting a blue semi truck" style="left:140px;top:86px;width:471px;height:335px"></div>
  <div class="section-title abs" style="left:648px;top:96px"><span class="accent">About</span> <span style="color:var(--black)">us</span></div>
  <p class="body-text abs" style="left:648px;top:168px;width:410px;height:225px;overflow:hidden;text-align:justify">Lorem ipsum dolor sit amet, consectetur adipiscing elit. Quid autem habent admirationis, cum prope accesseris? An hoc usque quaque, aliter in vita? Non igitur de improbo, sed de callido improbo quaerimus, qualis Q. Nam quibus rebus efficiuntur voluptates, eae non sunt in potestate sapientis. Negare non possum. Huic mori optimum esse propter desperationem sapientiae, illi propter spem vivere. Quid enim me prohiberet Epicureum esse, si probarem, quae ille diceret? Qui-vere falsone, quaerere mittimus-dicitur oculis se</p>
  <span class="btn abs" style="left:648px;top:393px;width:124px">Learn more</span>
</section>

<section class="services abs">
  <div class="section-title centered abs" style="top:86px"><span class="accent">Our</span> <span>services</span></div>
  <p class="body-text abs" style="left:118px;top:168px;width:964px">Lorem ipsum dolor sit amet, consectetur adipiscing elit. Quid autem habent admirationis, cum prope accesseris? An hoc usque quaque, aliter in vita? Non igitur de improbo, sed de callido improbo quaerimus, qualis Q. Nam quibus rebus efficiuntur voluptates, eae non sunt in potestate sapientis. Negare non possum. Huic mori optimum esse propter desperationem sapientiae, illi propter spem vivere. Quid enim me prohiberet Epicureum esse, si probarem, quae ille diceret?</p>
  <svg class="abs" style="left:46px;top:370px" width="24" height="44" viewBox="0 0 24 44"><path d="M20 2 L4 22 L20 42" fill="none" stroke="#999" stroke-width="2"/></svg>
  <svg class="abs" style="left:1130px;top:370px" width="24" height="44" viewBox="0 0 24 44"><path d="M4 2 L20 22 L4 42" fill="none" stroke="#999" stroke-width="2"/></svg>
  <div class="service abs" style="left:95px;top:283px">
    <div class="circle" role="img" aria-label="Photo of a parking officer in a high-visibility vest" style="background:radial-gradient(circle,#b8c24a,#5e6f82)"></div>
    <h3>PARKING ENFORCEMENT</h3>
    <p>Lorem ipsum dolor sit amet, consectetur adipiscing elit. Quid</p>
    <span class="btn">Learn more</span>
  </div>
  <div class="service abs" style="left:355px;top:283px">
    <div class="circle" role="img" aria-label="Photo of a car wheel with a clamp" style="background:radial-gradient(circle,#e8e8e8,#8e8e8e)"></div>
    <h3>REPOSSESSION</h3>
    <p>Lorem ipsum dolor sit amet, consectetur adipiscing elit. Quid</p>
    <span class="btn">Learn more</span>
  </div>
  <div class="service abs" style="left:615px;top:283px">
    <div class="circle" role="img" aria-label="Photo of a warning triangle on a snowy road" style="background:radial-gradient(circle,#c9483e,#7f9cb6 55%,#dfe6ee)"></div>
    <h3>BREAKDOWN ASSISTANCE</h3>
    <p>Lorem ipsum dolor sit amet, consectetur adipiscing elit. Quid</p>
    <span class="btn">Learn more</span>
  </div>
  <div class="service abs" style="left:875px;top:283px">
    <div class="circle" role="img" aria-label="Photo of a cracked windshield after an accident" style="background:radial-gradient(circle,#8fa3ad,#3d4a55 60%,#7a5a40)"></div>
    <h3>ACCIDENT RECOVERY</h3>
    <p>Lorem ipsum dolor sit amet, consectetur adipiscing elit. Quid</p>
    <span class="btn">Learn more</span>
  </div>
</section>

<section class="news abs">
  <div class="col-title abs" style="left:70px;top:73px">LATEST BLOG</div>
  <div class="pager abs" style="left:524px;top:78px"><span>‹</span><span class="dark">›</span></div>
  <div class="rule abs" style="left:70px;top:122px;width:500px"></div>
  <div class="photo abs" role="img" aria-label="Photo of a tow truck loading a car" style="left:70px;top:157px;width:110px;height:112px;background:linear-gradient(135deg,#6c95bf,#d9dfe5 60%,#8a8f95)"></div>
  <div class="post-title abs" style="left:198px;top:155px">Non igitur de improbo, sed de callido improbo</div>
  <p class="small-text abs" style="left:198px;top:182px;width:372px;height:64px;overflow:hidden">Lorem ipsum dolor sit amet, consectetur adipiscing elit. Quid autem habent admirationis, cum prope accesseris? An hoc usque quaque, aliter in vita? Non igitur de improbo, sed de callido improbo quaerimus, qualis Q. Nam quibus rebus efficiuntur voluptates, eae non sunt in potestate sapien</p>
  <div class="abs" style="left:198px;top:253px;font-size:11px;color:var(--black)">Posted By Website Admin - 23-05-2019</div>
  <div class="abs" style="left:498px;top:253px;font-size:11px;color:var(--red)">Read more »</div>
  <div class="abs" style="left:598px;top:70px;width:1px;height:235px;background:#ccc"></div>
  <div class="col-title abs" style="left:628px;top:73px">TESTIMOINALS</div>
  <div class="pager abs" style="left:1082px;top:78px"><span>‹</span><span class="dark">›</span></div>
  <div class="rule abs" style="left:628px;top:122px;width:500px"></div>
  <div class="abs" role="img" aria-label="Portrait photo of a smiling customer" style="left:628px;top:157px;width:110px;height:112px;background:linear-gradient(160deg,#d9c4b3,#a98a73)"></div>
  <p class="small-text abs" style="left:752px;top:155px;width:376px"><b style="color:var(--black)">“</b>Lorem ipsum dolor sit amet, consectetur adipiscing elit. Quidautem habent admirationis, cum prope accesseris? An hoc usque quaque, aliter in vita? Non igitur de improbo, sed de callido improbo quaerimus, qualis Q. Nam quibus rebus efficiuntur voluptates, eae non sunt in potestate sapientis. Negare non possum. Huic mori optimum esse propter desperationem sapientiae, illi propter spem vivere.<b style="color:var(--black)">”</b></p>
  <div class="abs" style="left:752px;top:258px;font-size:11px;font-weight:700;color:var(--red)">- MARLENE</div>
</section>

<section class="contact abs">
  <div class="section-title centered abs" style="top:70px"><span class="accent">Contact</span> <span>us</span></div>
</section>
<div class="form-card abs">
  <div class="field abs" style="left:56px;top:67px;width:262px;height:37px">Name</div>
  <div class="field abs" style="left:328px;top:67px;width:262px;height:37px">Email</div>
  <div class="field abs" style="left:600px;top:67px;width:262px;height:37px">Phone</div>
  <div class="field abs" style="left:56px;top:115px;width:806px;height:102px">Message</div>
  <div class="submit abs" style="left:56px;top:234px;width:806px">Submit</div>
</div>

<section class="newsletter abs">
  <svg class="abs" style="left:70px;top:17px" width="32" height="32" viewBox="0 0 32 32"><circle cx="16" cy="16" r="16" fill="#fff"/><rect x="8" y="10" width="16" height="12" fill="none" stroke="#0b0b0d" stroke-width="2"/><path d="M8 10 L16 17 L24 10" fill="none" stroke="#0b0b0d" stroke-width="2"/></svg>
  <div class="abs" style="left:128px;top:18px;font-size:24px">News letter Signup</div>
  <div class="abs" style="left:356px;top:18px;width:633px;height:30px;background:#fff;color:#555;font-size:12px;padding:8px 12px">Enter Your Email</div>
  <div class="abs" style="left:998px;top:18px;width:126px;height:30px;background:var(--black);color:#fff;font-size:13px;font-weight:700;text-align:center;line-height:30px">SUBSCRIBE</div>
</section>

<footer class="footer abs">
  <div class="brand abs" style="left:72px;top:42px">Bergungsdienst<small>Talwald Ost</small></div>
  <p class="small-text abs" style="left:72px;top:150px;width:250px;color:#ccc;text-align:justify">Lorem ipsum dolor sit amet, consectetur adipiscing. Quidautem habent admirationis, cum prope accesseris? An hoc usque quaque, aliter in vita? Non igitur de improbo, sed de callido improbo quaerimus, qualis Q. Nam quibus rebus efficiuntur voluptates, eae non sunt in</p>
  <div class="foot-title abs" style="left:400px;top:50px"><span class="accent">Quick</span> Links</div>
  <div class="abs" style="left:400px;top:80px;width:185px;height:1px;background:#444"></div>
  <ul class="foot-list abs" style="left:400px;top:92px">
    <li>Home</li><li>About us</li><li>Parking Enforcement</li><li>Repossession</li><li>breakdown assistance</li><li>Accident Recovery</li>
  </ul>
  <div class="foot-title abs" style="left:664px;top:50px"><span class="accent">Contact</span> Us</div>
  <div class="abs" style="left:664px;top:80px;width:185px;height:1px;background:#444"></div>
  <div class="foot-info abs" style="left:664px;top:98px">1420 Birch Lane<br>Millbrook, IL 60321</div>
  <div class="foot-info abs" style="left:664px;top:158px">
    <div>✆&nbsp; (630) 555-0142</div>
    <div>▯&nbsp; (630) 555-0142</div>
    <div>✉&nbsp; info@bergungsdienst-talwald.cc</div>
    <div>●&nbsp; www.bergungsdienst-talwald.cc</div>
  </div>
  <div class="foot-title abs" style="left:930px;top:50px"><span class="accent">Follow Us</span> On</div>
  <div class="abs" style="left:930px;top:80px;width:185px;height:1px;background:#444"></div>
  <div class="social abs" style="left:930px;top:100px"><span style="background:#fff"></span><span style="background:#fff"></span><span style="background:#fff"></span><span style="background:#fff"></span><span style="background:#fff"></span><span style="background:#fff"></span></div>
  <div class="abs" style="left:930px;top:150px;width:20px;height:2px;background:#888"></div>
  <div class="abs" style="left:930px;top:196px;font-size:22px;font-weight:700;line-height:26px"><span style="color:var(--red)">CALL US ON</span><br>044 927 64 18</div>
</footer>
<div class="copyright abs">© 2017 Bergungsdienst Talwald Ost | Privacy Policy | User Agreement</div>

</body>
</html>
```